The Pulp Corner- 2026 Menu- Drinks/Food

We are The Pulp Corner, a premium NYC-inspired juice bar.
We need two matching 4K TV menu designs with a clean, modern New York feel.
TV 1 – DRINKS
Cold-Pressed Juices, Smoothies, and Coffee/Espresso.
TV 2 – FOOD
Bowls, Toasts, Wraps, Hot Food, and Treats/Sweets.
The menus should feel bold, minimal, and easy to read from a distance.
Strong typography is preferred over heavy photos. The two screens must clearly match as one brand while serving different purposes.
Designs must be optimized for 4K TVs and in a NYC style (subtle subway / street influence, not cartoonish).
This is what we have now. We are updating items and prices along with changing some items.
I have some changes we’d like to do also. But this is what we are using now

```html
<!DOCTYPE html>
<html lang="en">
<head>
<meta charset="utf-8">
<title>The Pulp Corner – Menu Boards</title>
<link href="https://fonts.googleapis.com/css2?family=Bebas+Neue&family=Kaushan+Script&family=Roboto:wght@400;500&display=swap" rel="stylesheet">
<style>
  :root {
    --page: #e9e9e9;
    --board: #262626;
    --board-deep: #1d1d1d;
    --band: #141414;
    --yellow: #f5b21b;
    --white: #ffffff;
    --muted: #d6d6d6;
    --rule: #8a8a8a;
    --ink: #1a1a1a;
  }
  * { box-sizing: border-box; margin: 0; padding: 0; }
  html, body { width: 1200px; height: 1152px; overflow: hidden; background: var(--page); }
  body { padding: 12px; display: flex; flex-direction: column; gap: 12px; font-family: "Roboto", Arial, sans-serif; }

  .board {
    position: relative;
    width: 1176px; height: 558px;
    background: var(--board);
    color: var(--white);
    overflow: hidden;
  }
  .board-band {
    height: 62px;
    background: var(--band);
    display: flex; align-items: flex-end; justify-content: center;
  }
  .brand {
    font-family: "Bebas Neue", Arial, sans-serif; font-weight: 400;
    font-size: 52px; line-height: 1; letter-spacing: 1px;
    color: var(--white);
    padding-bottom: 4px;
  }
  .board-title { position: relative; height: 30px; }
  .board-title::before {
    content: ""; position: absolute; left: 0; right: 0; top: 4px; height: 2px; background: var(--yellow);
  }
  .board-title span {
    position: absolute; left: 50%; transform: translateX(-50%); top: 0;
    background: var(--board); padding: 0 10px;
    font-family: "Bebas Neue", Arial, sans-serif; font-size: 30px; line-height: 1;
  }
  .board-body { display: grid; gap: 22px; padding: 8px 18px 0; }
  .drinks .board-body { grid-template-columns: 1fr 1fr 1fr 0.88fr; }
  .foods .board-body { grid-template-columns: 1fr 1fr 0.82fr 0.82fr; }

  .column { display: flex; flex-direction: column; }

  .photo-pair { display: flex; gap: 4px; height: 60px; margin-bottom: 4px; }
  .photo { flex: 1; border: 1px solid var(--white); }
  .photo-tall { height: 150px; border: 1px solid #555; margin-bottom: 8px; }
  .photo-food { height: 146px; border: 2px solid var(--white); margin-bottom: 7px; }

  .section-head { display: flex; align-items: flex-end; gap: 4px; margin: 2px 0 4px; }
  .section-head h2 { font-family: "Kaushan Script", cursive; font-weight: 400; font-size: 19px; line-height: 1; white-space: nowrap; }
  .section-head::after { content: ""; flex: 1; border-bottom: 1px dashed var(--rule); margin-bottom: 3px; }

  .item { margin-bottom: 4px; }
  .item-head { display: flex; justify-content: space-between; align-items: baseline; }
  .item-name, .price {
    font-family: "Bebas Neue", Arial, sans-serif; font-size: 12.5px; line-height: 1.05; color: var(--yellow); letter-spacing: .2px;
  }
  .item-desc { font-size: 7.5px; line-height: 1.15; color: var(--muted); padding-right: 44px; }

  .coffee-row { display: flex; justify-content: space-between; align-items: baseline; }
  .coffee-row .sizes { font-family: "Bebas Neue", Arial, sans-serif; font-size: 12.5px; color: var(--white); }
  .addon { font-size: 7.5px; color: var(--muted); display: flex; justify-content: space-between; align-items: baseline; margin: 3px 0; }

  .note { background: var(--yellow); color: var(--ink); text-align: center; font-size: 7.5px; padding: 4px; margin: 10px 0 3px; }
  .note-strong { text-align: center; font-size: 8px; font-weight: 500; line-height: 1.3; margin-bottom: 10px; }
  .note-strong b { color: var(--yellow); font-weight: 500; }

  .custom-box { margin-top: 4px; border: 1px solid var(--yellow); }
  .custom-box .tag { background: var(--yellow); color: var(--ink); font-family: "Bebas Neue", Arial, sans-serif; font-size: 12px; padding: 1px 5px; }
  .custom-box p { font-size: 7.5px; color: var(--muted); padding: 2px 5px; }

  .mixins { list-style: none; }
  .mixins li { display: flex; justify-content: space-between; align-items: baseline; }
  .mixins .item-name, .mixins .price { font-size: 11px; line-height: 1.2; }
  .mixins small { display: block; font-size: 7.5px; line-height: 1.1; color: var(--muted); font-family: "Roboto", Arial, sans-serif; }
</style>
</head>
<body>

<section class="board drinks">
  <header class="board-band"><h1 class="brand">The Pulp Corner</h1></header>
  <div class="board-title"><span>Drinks</span></div>
  <div class="board-body">

    <div class="column">
      <div class="photo-pair">
        <div class="photo" role="img" aria-label="Bottled fresh juices in a row" style="background:linear-gradient(120deg,#6f8a3a,#d85a2a,#e9a33a)"></div>
        <div class="photo" role="img" aria-label="Juice jars on a beach" style="background:linear-gradient(120deg,#7fb4d8,#b0455a,#e8c08a)"></div>
      </div>
      <div class="section-head"><h2>Cold Pressed Juices</h2></div>
      <div class="item"><div class="item-head"><span class="item-name">Hot Bam (S)</span><span class="price">$12.50</span></div><p class="item-desc">Red Apple, Lemon, Ginger, Cayenne Pepper</p></div>
      <div class="item"><div class="item-head"><span class="item-name">Sunset Park</span><span class="price">$12.50</span></div><p class="item-desc">Orange, Carrot, Celery</p></div>
      <div class="item"><div class="item-head"><span class="item-name">Lean Green</span><span class="price">$12.50</span></div><p class="item-desc">Spinach, Celery, Cucumber, Romaine, Lemon, Himalayan Pink Salt</p></div>
      <div class="item"><div class="item-head"><span class="item-name">Revive</span><span class="price">$12.50</span></div><p class="item-desc">Cantaloupe, Red Apple, Lemon</p></div>
      <div class="item"><div class="item-head"><span class="item-name">Renew</span><span class="price">$12.50</span></div><p class="item-desc">Coconut Water, Red Apple, Blueberry, Grape</p></div>
      <div class="item"><div class="item-head"><span class="item-name">Vida</span><span class="price">$12.50</span></div><p class="item-desc">Beet, Raspberry, Red Apple, Orange</p></div>
      <div class="item"><div class="item-head"><span class="item-name">The Breakdown</span><span class="price">$12.50</span></div><p class="item-desc">Carrot, Red Apple, Ginger, Beet, Lemon, Pineapple</p></div>
      <div class="item"><div class="item-head"><span class="item-name">Green Goddess</span><span class="price">$12.50</span></div><p class="item-desc">Spinach, Celery, Cucumber, Romaine, Kale, Parsley, Green Cabbage</p></div>
      <div class="item"><div class="item-head"><span class="item-name">Sunny Day</span><span class="price">$12.50</span></div><p class="item-desc">Pineapple, Lemon, Orange, Ginger</p></div>
      <div class="item"><div class="item-head"><span class="item-name">Glow Up</span><span class="price">$13.00</span></div><p class="item-desc">Celery, Lime</p></div>
      <div class="item"><div class="item-head"><span class="item-name">Sailor's Delight</span><span class="price">$12.50</span></div><p class="item-desc">Spinach, Orange, Pear, Green Apple, Ginger</p></div>
      <div class="item"><div class="item-head"><span class="item-name">Classic (Shot)</span><span class="price">$6.00</span></div><p class="item-desc">Ginger, Lemon</p></div>
    </div>

    <div class="column">
      <div class="item"><div class="item-head"><span class="item-name">Sunshine (Shot)</span><span class="price">$6.00</span></div><p class="item-desc">Ginger, Lemon, Red Apple, Turmeric, Black Pepper</p></div>
      <div class="item"><div class="item-head"><span class="item-name">Green Bolt (Shot)</span><span class="price">$6.00</span></div><p class="item-desc">Ginger, Lemon, Cayenne Pepper, Spinach, Green Apple</p></div>
      <div class="item"><div class="item-head"><span class="item-name">Detox (Shot)</span><span class="price">$6.00</span></div><p class="item-desc">Wheatgrass</p></div>
      <div class="photo-pair" style="margin-top:4px">
        <div class="photo" role="img" aria-label="Fruit smoothies with citrus" style="background:linear-gradient(120deg,#e9d27a,#c8a4d8,#f3f0e4)"></div>
        <div class="photo" role="img" aria-label="Layered smoothies by the sea" style="background:linear-gradient(120deg,#7fc0d8,#e58aa0,#f0b050)"></div>
      </div>
      <div class="section-head"><h2>Smoothies</h2></div>
      <div class="item"><div class="item-head"><span class="item-name">Spring Street</span><span class="price">$13.00</span></div><p class="item-desc">Coconut Water, Blueberries, Pineapple, Spinach, Honey, Hemp Hearts</p></div>
      <div class="item"><div class="item-head"><span class="item-name">Flushing Ave</span><span class="price">$13.00</span></div><p class="item-desc">Coconut Milk, Spinach, Kale, Strawberries, Pineapple, Chia Seeds, Hemp Hearts</p></div>
      <div class="item"><div class="item-head"><span class="item-name">Fort Greene</span><span class="price">$13.00</span></div><p class="item-desc">Almond Milk, Bananas, Mango, Avocado, Spinach, Kale, Honey</p></div>
      <div class="item"><div class="item-head"><span class="item-name">Jimmy the Leafy Legend</span><span class="price">$13.00</span></div><p class="item-desc">Coconut Milk, Bananas, Strawberries, Kale, Sea Moss Gel, Green Spirulina</p></div>
      <div class="item"><div class="item-head"><span class="item-name">Atlantic Terminal</span><span class="price">$13.00</span></div><p class="item-desc">Almond Milk, Bananas, Strawberries, Blueberries, Pineapple, Coconut Shavings; Choice of 1 of the following: Peanut, Almond, Cashew Butter and/or Hazelnut Spread, Honey, Chia Seeds, Bee Pollen</p></div>
      <div class="item"><div class="item-head"><span class="item-name">Union Square</span><span class="price">$13.00</span></div><p class="item-desc">Almond Milk, Grade A Açai, Bananas, Strawberries, Blueberries, Pineapple, Coconut Oil</p></div>
      <div class="item"><div class="item-head"><span class="item-name">Grand Central</span><span class="price">$13.00</span></div><p class="item-desc">Almond Milk, Grade A Açai, Bananas, Blueberries, Granola, Cacao Nibs; Choice of 1 of the following: Peanut, Almond, Cashew Butter and/or Hazelnut Spread</p></div>
    </div>

    <div class="column">
      <div class="item"><div class="item-head"><span class="item-name">P.S. 124</span><span class="price">$12.00</span></div><p class="item-desc">1 liquid base: Almond, Coconut and/or Oat Milk, Orange Juice, Apple Juice or Coconut Water; Bananas and Strawberries</p></div>
      <div class="item"><div class="item-head"><span class="item-name">Lexington Avenue</span><span class="price">$12.50</span></div><p class="item-desc">Coconut Milk, Strawberries, Bananas, Raspberries, Kiwi, Vanilla Yogurt</p></div>
      <div class="item"><div class="item-head"><span class="item-name">Power Up</span><span class="price">$13.00</span></div><p class="item-desc">Almond Milk, Bananas, Strawberries, Raspberries, Peanut Butter, Cacao Nibs</p></div>
      <div class="item"><div class="item-head"><span class="item-name">The "Cawfee" Smoothie</span><span class="price">$13.00</span></div><p class="item-desc">Cold Brew Coffee, Almond Milk, Bananas, Vanilla Plant Protein, Cacao Nibs, Agave</p></div>
      <div class="item"><div class="item-head"><span class="item-name">The Peanut</span><span class="price">$12.50</span></div><p class="item-desc">Almond Milk, Bananas, Peanut Butter, Cinnamon, Chocolate Plant Protein</p></div>
      <div class="item"><div class="item-head"><span class="item-name">Build Your Own</span><span class="price">$12.00</span></div><p class="item-desc">1 liquid base: Almond, Coconut, Oat Milk, Orange, Apple Juice, Coconut Water, Filtered Water; Choice of 3 Fruits and/or Vegetables.</p></div>
      <div class="photo-pair" style="margin-top:4px">
        <div class="photo" role="img" aria-label="Berry yogurt parfaits" style="background:linear-gradient(120deg,#f2ece6,#c0304a,#f4f0ea)"></div>
        <div class="photo" role="img" aria-label="Parfait cups with granola" style="background:linear-gradient(120deg,#e8e2da,#b08a5a,#f0ece6)"></div>
      </div>
      <div class="section-head"><h2>Parfaits &amp; Treats</h2></div>
      <div class="item"><div class="item-head"><span class="item-name">Liberty Stack</span><span class="price">$9.00</span></div><p class="item-desc">Vanilla Yogurt, Granola, Strawberries, Blueberries, Coconut Flakes, Honey, Hemp Hearts</p></div>
      <div class="item"><div class="item-head"><span class="item-name">Build Your Own Parfait</span><span class="price">$8.00</span></div><p class="item-desc">Vanilla Yogurt, Granola, Choice of 2 Fruits, Honey</p></div>
      <div class="item"><div class="item-head"><span class="item-name">Protein Bites</span><span class="price">$6.25</span></div><p class="item-desc">Gluten Free Oats, Peanut Butter, Chia, Cacao Flax, Goji Berries, Chocolate Plant Protein, Maple Syrup &amp; Vanilla</p></div>
      <div class="item"><div class="item-head"><span class="item-name">Overnight Oats</span><span class="price">$9.00</span></div><p class="item-desc">Coconut Milk, Greek Yogurt, Chia Seeds, Vanilla Extract, Maple Syrup, Choice of 2 Fruit Toppings, Coconut Flakes, Honey, Cinnamon</p></div>
    </div>

    <div class="column">
      <div class="coffee-row"><span class="item-name">Cold Brew Coffee</span><span class="sizes">(12 oz) <span class="price">$5.50</span></span></div>
      <div class="coffee-row"><span></span><span class="sizes">(16 oz) <span class="price">$7.50</span></span></div>
      <div class="addon"><span>Almond Milk, Coconut Milk, Agave or Vanilla (each) +</span><span class="price">$0.75</span></div>
      <div class="coffee-row"><span class="item-name">Alkaline Water</span><span class="price">$3.00</span></div>
      <div class="coffee-row"><span class="item-name">Coconut Water</span><span class="price">$5.50</span></div>
      <p class="note">12 Oz Juices and 2 Oz Shots served in glass bottles.</p>
      <p class="note-strong"><b>Gallon</b> and <b>1/2 Gallon</b> of our signature juices available upon request.</p>
      <div class="photo-tall" role="img" aria-label="Granola and caramel shakes in tall glasses" style="background:linear-gradient(150deg,#3a3a3a,#a8743a,#e8dcc4)"></div>
      <div class="photo-tall" role="img" aria-label="Red, green and orange iced drinks" style="background:linear-gradient(110deg,#a0203a,#5fbf3a,#e8742a)"></div>
    </div>

  </div>
</section>

<section class="board foods">
  <header class="board-band"><h1 class="brand">The Pulp Corner</h1></header>
  <div class="board-title"><span>Foods</span></div>
  <div class="board-body">

    <div class="column">
      <div class="photo-pair">
        <div class="photo" role="img" aria-label="Grilled wraps on a board" style="background:linear-gradient(120deg,#c89a5a,#6f8a3a,#d8b07a)"></div>
        <div class="photo" role="img" aria-label="French toast with berries" style="background:linear-gradient(120deg,#b0602a,#e8c08a,#9a2a2a)"></div>
      </div>
      <div class="section-head"><h2>Toasts &amp; Wraps</h2></div>
      <div class="item"><div class="item-head"><span class="item-name">The Patriot</span><span class="price">$13.25</span></div><p class="item-desc">Seedy Sourdough Bread, Choice of Peanut, Almond, Cashew Butter or Hazelnut Spread, Strawberries, Bananas, Blueberries, Honey, Hemp Hearts</p></div>
      <div class="item"><div class="item-head"><span class="item-name">Avocado Toast</span><span class="price">$14.00</span></div><p class="item-desc">Seedy Sourdough Bread, Whole Avocado, Everything Bagel Seasoning, Honey</p></div>
      <div class="item"><div class="item-head"><span class="item-name">Breakfast Toast</span><span class="price">$14.50</span></div><p class="item-desc">Seedy Sourdough Bread, Smashed Avocado, Hard Boiled Eggs, Red Onion, Lemon Juice, Himalayan Pink Salt, Pepper, Everything Bagel Seasoning</p></div>
      <div class="item"><div class="item-head"><span class="item-name">Smoked Salmon Toast</span><span class="price">$15.00</span></div><p class="item-desc">Seedy Sourdough Bread, Smoked Wild Salmon, Tamari Sauce, Avocado, Cucumber, Leafy Greens, Everything Bagel Seasoning</p></div>
      <div class="item"><div class="item-head"><span class="item-name">Turmeric Chicken Salad</span><span class="price">$15.00</span></div><p class="item-desc">Wholewheat Sprouted Grain Wrap, Mayo, Chicken Breast, Red Onion, Cucumber, Carrots, Leafy Greens, Served with Balsamic Vinegar Dressing</p></div>
      <div class="item"><div class="item-head"><span class="item-name">Elite Wild Tuna Salad</span><span class="price">$15.00</span></div><p class="item-desc">Wholewheat Sprouted Grain Wrap, Mayo, Wild Tuna, Red Onion, Celery, Leafy Greens</p></div>
      <div class="item"><div class="item-head"><span class="item-name">Spicy Chickpea Salad (V)(S)</span><span class="price">$14.00</span></div><p class="item-desc">Wholewheat Sprouted Grain Wrap, Tomatillo Sriracha, Chickpeas, Toasted Sesame Seeds, Carrots, Leafy Greens, Red Pepper Hummus, Leafy Greens</p></div>
      <div class="custom-box">
        <div class="tag">*Custom Salads</div>
        <p>Available upon request depending on availability</p>
      </div>
    </div>

    <div class="column">
      <div class="photo-pair">
        <div class="photo" role="img" aria-label="Açai bowl with banana and granola" style="background:linear-gradient(120deg,#4a2a4a,#c8903a,#e8d8a8)"></div>
        <div class="photo" role="img" aria-label="Pink pitaya bowl with fruit" style="background:linear-gradient(120deg,#f0e8ee,#d83a8a,#8a2a6a)"></div>
      </div>
      <div class="section-head"><h2>Bowls</h2></div>
      <div class="item"><div class="item-head"><span class="item-name">Park Slope</span><span class="price">$13.50</span></div><p class="item-desc">Grade A Açai, Granola, Bananas, Honey</p></div>
      <div class="item"><div class="item-head"><span class="item-name">Bay Ridge</span><span class="price">$14.00</span></div><p class="item-desc">Grade A Açai, Granola, Bananas, Strawberries, Blueberries, Honey</p></div>
      <div class="item"><div class="item-head"><span class="item-name">Bushwick</span><span class="price">$14.25</span></div><p class="item-desc">Grade A Açai, Granola, Bananas, Pineapple, Fresh Coconut Meat, Honey, Bee Pollen</p></div>
      <div class="item"><div class="item-head"><span class="item-name">Main Street</span><span class="price">$14.00</span></div><p class="item-desc">Grade A Açai, Choice of 1 of the following: Peanut, Almond, Cashew Butter and/or Hazelnut Spread, Granola, Bananas, Honey, Cacao Nibs, Hemp Hearts</p></div>
      <div class="item"><div class="item-head"><span class="item-name">The Village</span><span class="price">$14.25</span></div><p class="item-desc">Grade A Açai, Granola, Bananas, Strawberries, Kiwi, Pineapple, Blueberries, Coconut Shavings, Honey, Hemp Hearts</p></div>
      <div class="item"><div class="item-head"><span class="item-name">Build Your Own</span><span class="price">$14.00</span></div><p class="item-desc">Grade A Açai, Granola, 2 Organic Fruits, Honey</p></div>
      <div class="item"><div class="item-head"><span class="item-name">Pink Pitaya</span><span class="price">$14.00</span></div><p class="item-desc">Apple Juice Blended w/ Pitaya, Bananas, Strawberries, Layered w/ Granola, Strawberries, Pineapple, Blueberries, Coconut Flakes, Honey, Hemp Hearts</p></div>
      <div class="item"><div class="item-head"><span class="item-name">Coco Loco</span><span class="price">$14.00</span></div><p class="item-desc">Coconut Milk blended w/ Coconut Chunks, Bananas, Honey. Layered w/ Granola, Pineapple, Seasonal Fruit, Fresh Coconut Meat, Coconut Flakes, Honey, Hemp Hearts</p></div>
      <div class="item"><div class="item-head"><span class="item-name">Coney Island</span><span class="price">$14.00</span></div><p class="item-desc">Apple Juice blended w/ Jackfruit, Mango and Pineapple, Layered w/ Granola, Bananas, Strawberries, Pineapple, Honey</p></div>
    </div>

    <div class="column">
      <div class="photo-pair">
        <div class="photo" role="img" aria-label="Fresh green salad" style="background:linear-gradient(120deg,#f0f0ec,#8ab03a,#e8c040)"></div>
        <div class="photo" role="img" aria-label="Smoked salmon toasts" style="background:linear-gradient(120deg,#f0ece8,#e8825a,#c86040)"></div>
      </div>
      <div class="section-head"><h2>Mix-ins</h2></div>
      <ul class="mixins">
        <li><span class="item-name">Honey</span><span class="price">$1.25</span></li>
        <li><span class="item-name">Extra Granola</span><span class="price">$2.00</span></li>
        <li><span class="item-name">Gluten Free Granola</span><span class="price">$2.25</span></li>
        <li><span class="item-name">Coconut Flakes</span><span class="price">$2.00</span></li>
        <li><span class="item-name">Coconut Oil</span><span class="price">$2.25</span></li>
        <li><span class="item-name">Bee Pollen</span><span class="price">$2.00</span></li>
        <li><span class="item-name">Peanut Butter</span><span class="price">$2.25</span></li>
        <li><span class="item-name">Almond Butter</span><span class="price">$2.50</span></li>
        <li><span class="item-name">Cashew Butter</span><span class="price">$2.75</span></li>
        <li><span class="item-name">Hazelnut Spread</span><span class="price">$2.75</span></li>
        <li><span class="item-name">Chia Seeds</span><span class="price">$2.00</span></li>
        <li><span class="item-name">Flax Seeds</span><span class="price">$2.00</span></li>
        <li><span class="item-name">Cacao Nibs</span><span class="price">$2.00</span></li>
        <li><span class="item-name">Hemp Hearts</span><span class="price">$2.00</span></li>
        <li><span class="item-name">Spirulina</span><span class="price">$2.00</span></li>
        <li><span class="item-name">Plant Protein<small>(Vanilla or Chocolate)</small></span><span class="price">$3.00</span></li>
        <li><span class="item-name">Whey Protein<small>(Vanilla or Chocolate)</small></span><span class="price">$3.25</span></li>
        <li><span class="item-name">Extra Açai</span><span class="price">$3.25</span></li>
        <li><span class="item-name">Maca Powder</span><span class="price">$2.50</span></li>
        <li><span class="item-name">Moringa Powder</span><span class="price">$2.75</span></li>
        <li><span class="item-name">Goji Berries</span><span class="price">$2.25</span></li>
        <li><span class="item-name">Vanilla Yogurt</span><span class="price">$2.75</span></li>
        <li><span class="item-name">Greek Yogurt</span><span class="price">$3.00</span></li>
        <li><span class="item-name">Avocado</span><span class="price">$3.25</span></li>
        <li><span class="item-name">Sea Moss Gel (V)</span><span class="price">$4.00</span></li>
      </ul>
    </div>

    <div class="column">
      <div class="photo-food" role="img" aria-label="Avocado toasts on a blue plate" style="background:radial-gradient(circle at 50% 55%,#7fa0b0 0%,#8aa040 35%,#f2f2f0 70%)"></div>
      <div class="photo-food" role="img" aria-label="Egg-in-toast with bacon" style="background:linear-gradient(120deg,#2a2a2a,#e8b060,#f0d040,#8a3020)"></div>
      <div class="photo-food" role="img" aria-label="Chickpea and vegetable salad bowl" style="background:radial-gradient(circle at 50% 55%,#c8903a 0%,#5f8a2a 40%,#e8e8e6 75%)"></div>
    </div>

  </div>
</section>

</body>
</html>
```